Business card for new business - financial management

I need a business card designed for my new business. I'm the owner / sole trader of QVB Consulting, which provides financial management services for Government. I'd like the design to incorporate the attached business name and colours. The design should include colour and not be too way out - it needs to look at home in a government environment.
Details to be included on the card are:
QVB Consulting
Miriam Haskett
0400 386 924
miriamrhaskett@fernmail.example
47 Pallister Crescent, Curtin ACT 2605
Single or double sided designs would be good.
Employees at Australian Federal Government agencies
Government

```html
<!DOCTYPE html>
<html lang="en">
<head>
<meta charset="utf-8">
<title>QVB Consulting – Business Card</title>
<link rel="stylesheet" href="https://fonts.googleapis.com/css2?family=Source+Sans+3:wght@400;600&display=swap">
<style>
  :root {
    --page-bg: #e9ecef;
    --card-bg: #ffffff;
    --navy: #2d4e80;
    --teal: #2e8a9c;
    --sky: #93cfdd;
    --ink: #2b2f33;
    --white: #ffffff;
  }
  html, body {
    margin: 0;
    padding: 0;
    width: 1200px;
    height: 1200px;
    overflow: hidden;
    background: var(--page-bg);
    font-family: "Source Sans 3", sans-serif;
  }
  .card {
    position: absolute;
    left: 100px;
    top: 314px;
    width: 1000px;
    height: 572px;
    background: var(--card-bg);
    box-shadow: 0 6px 24px rgba(0, 0, 0, 0.12);
    overflow: hidden;
  }
  .card-shapes {
    position: absolute;
    inset: 0;
  }
  .brand-name {
    position: absolute;
    left: 80px;
    top: 76px;
    margin: 0;
    font-size: 80px;
    font-weight: 600;
    line-height: 1;
    color: var(--navy);
    letter-spacing: 0.5px;
  }
  .holder-name {
    position: absolute;
    left: 600px;
    top: 176px;
    width: 400px;
    margin: 0;
    text-align: center;
    font-size: 40px;
    font-weight: 400;
    line-height: 72px;
    color: var(--white);
  }
  .contact-list {
    position: absolute;
    right: 265px;
    top: 262px;
    margin: 0;
    padding: 0;
    list-style: none;
    text-align: right;
    font-size: 28px;
    line-height: 38px;
    color: var(--ink);
  }
  .contact-list li { margin: 0; }
  .contact-list .gap { margin-top: 8px; }
  .contact-icons {
    position: absolute;
    left: 748px;
    top: 266px;
  }
</style>
</head>
<body>
  <main class="card">
    <svg class="card-shapes" width="1000" height="572" viewBox="0 0 1000 572" aria-hidden="true">
      <path class="contact-band" fill="var(--sky)"
            d="M0,400 L250,400 L300,262 Q306,248 322,248 L800,248 Q816,248 822,262 L858,360 Q864,378 846,384 L330,520 L0,520 Z"/>
      <path class="name-band" fill="var(--teal)"
            d="M1000,176 L640,176 L605,236 Q598,248 612,248 L1000,248 Z"/>
    </svg>

    <h1 class="brand-name">QVB Consulting</h1>
    <p class="holder-name">Miriam Haskett</p>

    <ul class="contact-list">
      <li>0400 386 924</li>
      <li>miriamrhaskett@fernmail.example</li>
      <li class="gap">47 Pallister Crescent</li>
      <li>Kelby ACT 2609</li>
    </ul>

    <svg class="contact-icons" width="40" height="140" viewBox="0 0 40 140" aria-hidden="true">
      <g class="icon-phone">
        <rect x="2" y="2" width="32" height="32" rx="7" fill="var(--teal)"/>
        <path d="M12 9 L15 9 L17 14 L15 16 Q17 20 21 22 L23 20 L28 22 L28 25 Q28 28 25 28 Q10 26 9 12 Q9 9 12 9 Z" fill="var(--white)"/>
      </g>
      <g class="icon-mail">
        <rect x="2" y="40" width="32" height="32" rx="7" fill="var(--teal)"/>
        <rect x="9" y="49" width="18" height="13" rx="1.5" fill="var(--white)"/>
        <path d="M9 50 L18 57 L27 50" fill="none" stroke="var(--teal)" stroke-width="1.8"/>
      </g>
      <g class="icon-pin">
        <rect x="2" y="88" width="32" height="32" rx="7" fill="var(--teal)"/>
        <path d="M18 115 Q10 105 10 100 A8 8 0 0 1 26 100 Q26 105 18 115 Z" fill="var(--white)"/>
        <circle cx="18" cy="100" r="3" fill="var(--teal)"/>
      </g>
    </svg>
  </main>
</body>
</html>
```